Innovative Healthcare Technology Company needs a Business Card Design

We are in need of an innovative business card design for a new healthcare software company called "Lumenwise Data Partners". We develop software that creates medical assessment applications and mobile e-learning prevention services to reduce risk behaviors in adolescent and young adults. Our initial product, the "KESTREL App", conducts a tailored sexual risk assessment and provides a doctor with an insightful patient report to improve sexual risk counseling and ultimately reduce unintended pregnancy, STDs, etc.

We would like the design to incorporate our logo and branding colors (attached) in an innovative and creative manner. The final design should communicate professionalism and healthcare innovation. Our tag line is "insight drives better care" (doesn't necessarily need to be included) and our target audience is doctors, medical directors, and medical business administrators. Please visit our website for additional info ourbrightmarq.com. Be creative and we look forward to seeing your designs!

Target Market(s)

healthcare - doctors, medical directors and medical business administrators

Industry/Entity Type

Healthcare

Contact Information for Business Card

We would like the design to incorporate our logo and branding colors (attached) in an innovative and creative manner. The final design should communicate professionalism and healthcare innovation. Our tag line is "insight drives better care" (doesn't necessarily need to be included)

Font styles to use
Other font styles liked:
• quicksand

Requirements
Must have
• our logo and brand colors
• Name, (Mara Feldhovenik, PhD)
• Email (drmara@ourbrightmarq.com)
• phone (555.283.9170)
• Website (ourbrightmarq.com)
Should not have
• cartoon look

```html
<!DOCTYPE html>
<html lang="en">
<head>
<meta charset="utf-8">
<title>Lumenwise Data Partners – Mara Feldhovenik</title>
<link rel="stylesheet" href="https://fonts.googleapis.com/css2?family=Quicksand:wght@500&family=PT+Sans&family=Open+Sans:wght@400&display=swap">
<style>
  :root {
    --bg: #ebebeb;
    --brand-blue: #0d5a9c;
    --brand-green: #3f9a83;
    --text: #4a4a4a;
    --card: #ffffff;
    --line: #d6d6d6;
    --icon-cut: #ffffff;
  }
  * { box-sizing: border-box; margin: 0; padding: 0; }
  html, body { width: 1200px; height: 750px; overflow: hidden; }
  body { background: var(--bg); position: relative; font-family: "Open Sans", sans-serif; color: var(--text); }

  .brand {
    position: absolute; left: 0; width: 1200px; top: 112px;
    display: flex; justify-content: center; align-items: center; gap: 14px;
  }
  .brand-square { width: 34px; height: 34px; background: var(--brand-blue); }
  .brand-name {
    font-family: "Quicksand", sans-serif; font-weight: 500;
    font-size: 34px; color: var(--brand-blue); letter-spacing: 0.5px;
  }

  .profile-photo {
    position: absolute; left: 406px; top: 277px; width: 106px; height: 118px;
    background: linear-gradient(180deg, #b3b3b3, #9c9c9c);
  }
  .person { position: absolute; left: 534px; top: 304px; font-family: "PT Sans", sans-serif; }
  .person-name { font-size: 28px; color: var(--brand-blue); letter-spacing: -0.3px; }
  .person-name .degree { font-size: 20px; }
  .person-title { font-size: 21px; color: var(--brand-green); margin-top: 6px; }

  .contact-card {
    position: absolute; left: 401px; top: 422px; width: 398px;
    background: var(--card); border: 1px solid var(--line); border-radius: 8px;
  }
  .contact-row {
    height: 59px; display: flex; align-items: center; justify-content: center; gap: 8px;
    font-size: 18px; border-bottom: 1px solid var(--line);
  }
  .contact-row:last-child { border-bottom: none; }
  .contact-row svg { width: 20px; height: 20px; fill: var(--brand-blue); }
  .contact-row .cut { fill: none; stroke: var(--icon-cut); }
  .tagline { font-size: 25px; letter-spacing: 0.3px; }
</style>
</head>
<body>
  <header class="brand">
    <span class="brand-square"></span>
    <span class="brand-name">Lumenwise Data Partners</span>
  </header>

  <div class="profile-photo" role="img" aria-label="Portrait photo of Mara Feldhovenik"></div>

  <div class="person">
    <p class="person-name">Mara Feldhovenik, <span class="degree">PhD</span></p>
    <p class="person-title">CEO/Founder</p>
  </div>

  <section class="contact-card">
    <div class="contact-row">
      <svg viewBox="0 0 24 24" aria-hidden="true"><path d="M6.6 2.5l3 3.4c.4.5.4 1.2 0 1.7L8 9.3c1.2 2.6 3.5 5 6.3 6.4l1.7-1.6c.5-.4 1.2-.4 1.7 0l3.4 2.9c.5.4.5 1.2.1 1.7l-1.7 2c-.6.7-1.6 1-2.5.7C10 19.6 4.6 14.3 2.6 7.5c-.3-.9 0-1.9.7-2.5l1.9-1.5c.4-.4 1-.4 1.4 0z"/></svg>
      <span>555.283.9170</span>
    </div>
    <div class="contact-row">
      <svg viewBox="0 0 24 24" aria-hidden="true"><rect x="2" y="5" width="20" height="14"/><path class="cut" d="M2.5 5.5l9.5 7.5 9.5-7.5" stroke-width="1.6"/></svg>
      <span>drmara@ourbrightmarq.com</span>
    </div>
    <div class="contact-row">
      <svg viewBox="0 0 24 24" aria-hidden="true"><circle cx="12" cy="12" r="10"/><path class="cut" d="M2 12h20M12 2c3 3 3 17 0 20M12 2c-3 3-3 17 0 20" stroke-width="1.4"/></svg>
      <span>www.ourbrightmarq.com</span>
    </div>
    <div class="contact-row">
      <span class="tagline">insight drives better care</span>
    </div>
  </section>
</body>
</html>
```